Website Design for Employee Moral and Happiness Company

Looking for a clean website design that explains our features in a step by step manner so our visitors know exactly what our site does before logging in.

The site is called "Velquo". See logo design and video for a sample of style and an overview of what we do.

Target Market(s)

Business owners that are looking to retain employees.

Number of Pages Required

1 page

```html
<!DOCTYPE html>
<html lang="en">
<head>
<meta charset="utf-8">
<title>Velquo — Happier teams, better events</title>
<link rel="stylesheet" href="https://fonts.googleapis.com/css2?family=Crimson+Pro:wght@600;700&family=Nunito+Sans:ital,wght@0,400;0,700;0,800;1,700&display=swap">
<style>
  :root {
    --bg: #e4dbc9;
    --header-bg: #e9e0d5;
    --band: #cdc2ad;
    --ink: #2e2e2e;
    --text: #555250;
    --muted: #6a6a6a;
    --accent: #ff6600;
    --tick: #5f5f5f;
    --rail: #7a7672;
    --art-dark: #071a2a;
    --art-blue: #21497a;
    --art-teal: #2aa7b3;
  }
  * { box-sizing: border-box; margin: 0; padding: 0; }
  html, body { width: 1200px; height: 698px; overflow: hidden; }
  body {
    position: relative;
    background: var(--bg);
    font-family: "Nunito Sans", sans-serif;
    color: var(--text);
  }

  .site-header {
    position: absolute; left: 0; top: 0;
    width: 1200px; height: 89px;
    background: var(--header-bg);
    border-bottom: 1px solid #efe8de;
  }
  .brand {
    position: absolute; left: 66px; top: 14px;
    font-family: "Crimson Pro", serif;
    font-weight: 700; font-size: 44px; line-height: 1;
    color: #111;
    letter-spacing: 0.5px;
  }
  .main-nav {
    position: absolute; top: 35px; left: 0;
    font-size: 16px; color: #333;
  }
  .main-nav a {
    position: absolute; white-space: nowrap;
    color: inherit; text-decoration: none;
  }
  .main-nav a.is-active {
    color: var(--accent);
    border-bottom: 1px solid var(--accent);
    line-height: 17px;
  }
  .login {
    position: absolute; left: 907px; top: 35px;
    font-size: 16px; color: #333;
    display: flex; align-items: center; gap: 9px;
  }
  .signup {
    position: absolute; left: 995px; top: 18px;
    width: 140px; height: 45px;
    border-radius: 23px;
    background: var(--accent);
    color: #fff;
    font-weight: 800; font-size: 16px;
    display: flex; align-items: center; justify-content: center;
    letter-spacing: 0.3px;
  }

  .ground-band { position: absolute; left: 0; top: 0; }

  .hero-art {
    position: absolute; left: -30px; top: 204px;
    width: 474px; height: 399px;
    border-radius: 0 200px 0 0;
    background: radial-gradient(circle at 55% 45%, var(--art-teal) 0%, var(--art-blue) 55%, var(--art-dark) 92%);
  }

  .problem {
    position: absolute; left: 656px; top: 228px;
  }
  .problem h1 {
    font-family: "Crimson Pro", serif;
    font-weight: 700; font-size: 34px; line-height: 35px;
    color: var(--ink);
  }
  .problem ul {
    list-style: none;
    margin-top: 36px;
  }
  .problem li {
    display: flex; align-items: center;
    height: 45.3px;
    font-size: 17px;
  }
  .problem li svg { flex: none; margin-right: 12px; }

  .section-rail { position: absolute; left: 1090px; top: 258px; }
  .rail-label {
    position: absolute; left: 1094px; top: 300px;
    font-size: 10px; line-height: 10px;
    font-style: italic; font-weight: 700;
    color: #333;
  }
</style>
</head>
<body>

<header class="site-header">
  <div class="brand">velquo</div>
  <nav class="main-nav">
    <a class="is-active" style="left:278px">Home</a>
    <a style="left:342px">Boring Work Events</a>
    <a style="left:499px">Introducing Velquo</a>
    <a style="left:654px">Why Velquo</a>
    <a style="left:767px">Testimonials</a>
  </nav>
  <div class="login">
    <svg width="13" height="12" viewBox="0 0 13 12" fill="none" stroke="#333" stroke-width="1.2">
      <path d="M1 6h7M5.5 3.5 8 6l-2.5 2.5M10 1h2v10h-2"/>
    </svg>
    Login
  </div>
  <div class="signup">SIGN UP</div>
</header>

<svg class="ground-band" width="1200" height="698" aria-hidden="true">
  <polygon points="0,544 428,698 0,698" fill="var(--band)"/>
</svg>

<div class="hero-art" role="img" aria-label="Illustration of a bored office worker resting his head on his hand at a desk in front of a monitor, with floating dashboard cards"></div>

<section class="problem">
  <h1>Boring coporate events<br>because of ?</h1>
  <ul>
    <li><svg width="23" height="23" viewBox="0 0 23 23"><circle cx="11.5" cy="11.5" r="11.5" fill="var(--tick)"/><path d="M7 11.8l3 3 6-6" fill="none" stroke="#fff" stroke-width="2.2"/></svg>Unhappy Employees who lacks moral boost</li>
    <li><svg width="23" height="23" viewBox="0 0 23 23"><circle cx="11.5" cy="11.5" r="11.5" fill="var(--tick)"/><path d="M7 11.8l3 3 6-6" fill="none" stroke="#fff" stroke-width="2.2"/></svg>Boring corporate events</li>
    <li><svg width="23" height="23" viewBox="0 0 23 23"><circle cx="11.5" cy="11.5" r="11.5" fill="var(--tick)"/><path d="M7 11.8l3 3 6-6" fill="none" stroke="#fff" stroke-width="2.2"/></svg>Lack of employee retention</li>
    <li><svg width="23" height="23" viewBox="0 0 23 23"><circle cx="11.5" cy="11.5" r="11.5" fill="var(--tick)"/><path d="M7 11.8l3 3 6-6" fill="none" stroke="#fff" stroke-width="2.2"/></svg>Complicated &amp; mediocre event planning tools</li>
    <li><svg width="23" height="23" viewBox="0 0 23 23"><circle cx="11.5" cy="11.5" r="11.5" fill="var(--tick)"/><path d="M7 11.8l3 3 6-6" fill="none" stroke="#fff" stroke-width="2.2"/></svg>Lack of employeer appreciation activities</li>
  </ul>
</section>

<svg class="section-rail" width="100" height="280" viewBox="1090 258 100 280" aria-hidden="true">
  <line x1="1175" y1="270" x2="1175" y2="518" stroke="var(--rail)" stroke-width="1.2"/>
  <g fill="var(--bg)" stroke="var(--rail)" stroke-width="1.4">
    <circle cx="1175" cy="270" r="5.5"/>
    <circle cx="1175" cy="352" r="5.5"/>
    <circle cx="1175" cy="394" r="5.5"/>
    <circle cx="1175" cy="435" r="5.5"/>
    <circle cx="1175" cy="476" r="5.5"/>
    <circle cx="1175" cy="518" r="5.5"/>
  </g>
  <circle cx="1175" cy="311" r="11" fill="#bdb5a8"/>
  <circle cx="1175" cy="311" r="6.5" fill="#2f2f2f"/>
</svg>
<div class="rail-label">Boring work<br>events</div>

</body>
</html>
```